Stationery design for pet company

We need a designer for stationery designs. The name of our company is Plimarv. We specialise in pet accessories as well as distribution of pet food. We also have a brand under us for our website called Tailwaggroove. We will need a letterhead for Plimarv and another for Tailwaggroove with matching envelopes. We also would like to have a business card design with name, contact details etc with the Plimarv logo on one side of the card. The other side of the business card should have the full logo of Tailwaggroove with our website www.tailwaggroove.example.

Target Market(s)

Stationery for Plimarv is for retail shops and suppliers, therefore should have a more professional feel. Stationery for Tailwaggroove is mainly for customers from the website.

Industry/Entity Type

Business

Requirements
Must have
• Preferably a use of black colour for the business card.
Nice to have
• Professional feel
Should not have
• Childish designs

```html
<!DOCTYPE html>
<html lang="en">
<head>
<meta charset="utf-8">
<title>Plimarv Business Card</title>
<link rel="stylesheet" href="https://fonts.googleapis.com/css2?family=Tinos:wght@400;700&display=swap">
<style>
  :root {
    --card-white: #ffffff;
    --ink-black: #000000;
    --brand-gold: #c99a4a;
    --text-grey: #6b6b6b;
    --logo-ink: #1c1c1c;
  }
  * { margin: 0; padding: 0; box-sizing: border-box; }
  html, body {
    width: 1200px;
    height: 677px;
    overflow: hidden;
    background: var(--card-white);
  }
  .business-card {
    position: relative;
    width: 1200px;
    height: 677px;
    background: var(--card-white);
    font-family: "Tinos", "Times New Roman", serif;
    overflow: hidden;
  }
  .footer-band {
    position: absolute;
    left: 0;
    top: 0;
    width: 1200px;
    height: 677px;
  }
  .brand-lockup {
    position: absolute;
    left: 72px;
    top: 318px;
    display: flex;
    align-items: center;
    gap: 18px;
  }
  .brand-dot {
    width: 36px;
    height: 36px;
    border-radius: 50%;
    background: var(--brand-gold);
  }
  .brand-name {
    font-weight: 700;
    font-size: 62px;
    letter-spacing: 6px;
    color: var(--logo-ink);
    line-height: 1;
    text-transform: uppercase;
  }
  .person {
    position: absolute;
    right: 82px;
    top: 44px;
    text-align: right;
    color: var(--text-grey);
  }
  .person-name {
    font-weight: 700;
    font-size: 55px;
    line-height: 1.05;
  }
  .person-role {
    font-weight: 400;
    font-size: 43px;
    line-height: 1.15;
    margin-right: 6px;
  }
  .contact-block {
    position: absolute;
    right: 102px;
    top: 312px;
    text-align: right;
    color: var(--text-grey);
    font-weight: 700;
    font-size: 32px;
    line-height: 41.5px;
    font-style: normal;
  }
  .footer-line {
    position: absolute;
    top: 605px;
    color: var(--card-white);
    font-weight: 700;
    font-size: 32px;
    line-height: 1;
  }
  .footer-email { left: 70px; }
  .footer-web { right: 102px; }
</style>
</head>
<body>
  <main class="business-card">
    <svg class="footer-band" viewBox="0 0 1200 677" aria-hidden="true">
      <path d="M0 490 Q600 684 1200 488 L1200 677 L0 677 Z" fill="var(--brand-gold)"/>
      <path d="M0 500 Q600 696 1200 497 L1200 677 L0 677 Z" fill="var(--ink-black)"/>
    </svg>

    <div class="brand-lockup">
      <span class="brand-dot"></span>
      <span class="brand-name">Plimarv</span>
    </div>

    <header class="person">
      <h1 class="person-name">Name Surname</h1>
      <p class="person-role">Designation</p>
    </header>

    <address class="contact-block">
      ab. sample street 46/2<br>
      65-960 sample town<br>
      tel: (123) 123-25-123<br>
      fax. +123 456 789
    </address>

    <p class="footer-line footer-email">email: email@email.com</p>
    <p class="footer-line footer-web">www.tailwaggroove.example</p>
  </main>
</body>
</html>
```